Web Design for Financial Consulting Company

We need a website design for a financial consulting company "Kelvane Consulting". We build financial models, scenario analysis, handle the budgeting process and provide temporary staffing. I have over 10 years of experience. My Excel expertise and analytical savvy has saved clients over $17 million in profit.

Target Market(s)

Small to medium businesses

Industry/Entity Type

Financial Consulting

Number of Pages Required

4 page

Requirements
Must have
• Professional looking
Nice to have
• A little futuristic looking

```html
<!DOCTYPE html>
<html lang="en">
<head>
<meta charset="utf-8">
<title>Kelvane Consulting</title>
<link href="https://fonts.googleapis.com/css2?family=Archivo+Black&family=Montserrat:wght@400;500;600;700&display=swap" rel="stylesheet">
<style>
:root{
  --navy:#0b3f66;
  --navy-deep:#05395c;
  --blue:#0a6fae;
  --sky:#12a7ec;
  --ink:#1b1d22;
  --field:#ebebeb;
  --white:#fff;
  --black:#000;
}
*{box-sizing:border-box;margin:0;padding:0}
html,body{width:1200px;height:3177px;overflow:hidden}
body{position:relative;font-family:"Montserrat",Arial,sans-serif;color:var(--ink);background:var(--white)}
.abs{position:absolute}
.display{font-family:"Archivo Black","Arial Black",sans-serif;text-transform:uppercase;letter-spacing:-1px}
.btn{position:absolute;display:flex;align-items:center;justify-content:center;font-family:"Archivo Black",sans-serif;font-size:11px;text-transform:uppercase;letter-spacing:.2px}
.btn-navy{background:linear-gradient(90deg,var(--navy-deep),var(--blue));color:var(--white)}
.btn-white{background:var(--white);color:var(--navy-deep)}

/* hero */
.hero{left:0;top:0;width:1200px;height:750px;background:radial-gradient(circle at 900px 360px,#2a6d86 0,#143a4c 18%,#1a2430 42%,#1c2026 70%,#24272c 100%)}
.hero-visual{left:700px;top:110px;width:440px;height:440px;border-radius:50%;background:radial-gradient(circle,rgba(150,235,255,.45) 0,rgba(60,170,210,.25) 40%,rgba(20,60,80,0) 70%)}
.brand{left:150px;top:27px;font-family:"Montserrat",sans-serif;font-weight:700;font-size:21px;color:var(--white);white-space:nowrap}
.nav{left:510px;top:33px;display:flex;gap:42px;font-size:13px;color:var(--white);text-transform:uppercase}
.nav .active{font-weight:700}
.nav-rule{left:150px;top:78px;width:905px;height:2px;background:rgba(255,255,255,.45)}
.hero-title{left:143px;top:208px;font-size:45px;line-height:57px;color:var(--white)}
.hero-title span{color:var(--sky)}
.hero-text{left:145px;top:400px;width:505px;font-size:12px;line-height:25px;color:#e6e6e6}

/* about */
.about-photo{left:140px;top:850px;width:450px;height:450px;border-radius:50%;background:linear-gradient(135deg,#d9c7d4,#8d8f95 50%,#4a4d52)}
.section-title{font-size:45px;color:var(--navy)}
.about-text{left:645px;top:983px;width:405px;font-size:12.5px;line-height:26.7px;color:var(--ink)}

/* services */
.services{left:0;top:1400px;width:1200px;height:673px;background:linear-gradient(120deg,#063d62,#0a72ad)}
.services .section-title{color:var(--white);width:1200px;text-align:center;top:105px}
.service{top:210px;width:190px;text-align:center;color:var(--white)}
.service-icon{width:100px;height:100px;border-radius:50%;background:var(--sky);margin:0 auto;display:flex;align-items:center;justify-content:center}
.service h3{font-family:"Archivo Black",sans-serif;font-size:20px;line-height:25px;text-transform:uppercase;margin-top:20px;letter-spacing:-.5px}
.service p{font-size:9.5px;line-height:18.5px;margin:14px auto 0;width:148px}
.divider{top:297px;width:2px;height:175px;background:rgba(255,255,255,.25)}

/* contact */
.field{left:150px;width:470px;height:40px;background:var(--field);font-size:11px;color:#333;padding:14px 0 0 37px}
.contact-photo{left:658px;top:2200px;width:450px;height:450px;border-radius:50%;background:linear-gradient(135deg,#bfc6cc,#8a6d5c 45%,#3d4a55)}

/* footer */
.footer{left:0;top:2848px;width:1200px;height:329px;background:var(--black);color:var(--white)}
.footer-brand{left:125px;top:110px;font-family:"Montserrat",sans-serif;font-weight:700;font-size:36px;color:var(--white);white-space:nowrap}
.copyright{left:125px;top:208px;font-size:16px}
.footer-nav{left:717px;top:116px;display:flex;gap:30px;font-size:16px}
.social{top:162px;width:56px;height:56px;border:2px solid var(--white);border-radius:50%}
</style>
</head>
<body>

<section class="abs hero">
  <div class="abs hero-visual" role="img" aria-label="Hand holding glowing digital gear interface"></div>
  <div class="abs brand">Kelvane Consulting</div>
  <nav class="abs nav"><span class="active">Home</span><span>About</span><span>Services</span></nav>
  <div class="btn btn-navy" style="left:880px;top:20px;width:167px;height:40px">Contact Us</div>
  <div class="abs nav-rule"></div>
  <h1 class="abs display hero-title">Helping your<br>finance team and<br>increasing <span>profit</span></h1>
  <p class="abs hero-text">Lorem Ipsum is simply dummy text of the printing and typesetting industry. Lorem Ipsum has been the industry's standard dummy text ever since the 1500s, when an unknown printer.</p>
  <div class="btn btn-white" style="left:145px;top:517px;width:185px;height:40px">Get Consultant</div>
</section>

<div class="abs about-photo" role="img" aria-label="Portrait of a consultant in a grey suit"></div>
<h2 class="abs display section-title" style="left:645px;top:905px">About Us</h2>
<p class="abs about-text">Lorem Ipsum is simply dummy text of the printing and typesetting industry. Lorem Ipsum has been the industry's standard dummy text ever since the 1500s, when an unknown printer took a galley of type and scrambled it to make a type specimen book. It has survived not only five centuries, but also the leap into electronic typesetting, remaining essentially unchanged.</p>
<div class="btn btn-navy" style="left:645px;top:1210px;width:167px;height:40px">Read More</div>

<section class="abs services">
  <h2 class="abs display section-title">Our Services</h2>

  <div class="abs service" style="left:100px">
    <div class="service-icon"><svg width="50" height="50" viewBox="0 0 50 50" fill="#fff"><rect x="6" y="30" width="6" height="14"/><rect x="16" y="24" width="6" height="20"/><rect x="26" y="18" width="6" height="26"/><rect x="36" y="10" width="6" height="34"/></svg></div>
    <h3>Financial<br>Models</h3>
    <p>Lorem Ipsum is simply dummy text of the printing and typesetting industry. Lorem Ipsum has been the</p>
  </div>
  <div class="abs divider" style="left:290px"></div>

  <div class="abs service" style="left:293px">
    <div class="service-icon"><svg width="50" height="50" viewBox="0 0 50 50" fill="none" stroke="#fff" stroke-width="4"><circle cx="15" cy="14" r="7"/><circle cx="35" cy="14" r="7"/><path d="M15 21v8l10 8 10-8v-8M8 42h34"/></svg></div>
    <h3>Budgeting<br>Process</h3>
    <p>Lorem Ipsum is simply dummy text of the printing and typesetting industry. Lorem Ipsum has been the</p>
  </div>
  <div class="abs divider" style="left:485px"></div>

  <div class="abs service" style="left:490px">
    <div class="service-icon"><svg width="50" height="50" viewBox="0 0 50 50" fill="#fff"><circle cx="25" cy="14" r="7"/><circle cx="11" cy="19" r="5"/><circle cx="39" cy="19" r="5"/><path d="M13 42c0-10 5-16 12-16s12 6 12 16zM3 40c0-7 3-12 8-12 2 0 4 1 5 2-2 3-3 6-3 10zM47 40c0-7-3-12-8-12-2 0-4 1-5 2 2 3 3 6 3 10z"/></svg></div>
    <h3>Temporary<br>Staffing</h3>
    <p>Lorem Ipsum is simply dummy text of the printing and typesetting industry. Lorem Ipsum has been the</p>
  </div>
  <div class="abs divider" style="left:690px"></div>

  <div class="abs service" style="left:698px">
    <div class="service-icon"><svg width="50" height="50" viewBox="0 0 50 50" fill="#fff"><rect x="8" y="32" width="6" height="10"/><rect x="18" y="26" width="6" height="16"/><rect x="28" y="20" width="6" height="22"/><rect x="38" y="28" width="6" height="14"/><rect x="5" y="44" width="40" height="3"/><circle cx="25" cy="10" r="6"/></svg></div>
    <h3>Process<br>Improvement</h3>
    <p>Lorem Ipsum is simply dummy text of the printing and typesetting industry. Lorem Ipsum has been the</p>
  </div>
  <div class="abs divider" style="left:903px"></div>

  <div class="abs service" style="left:908px;top:205px">
    <div class="service-icon"><svg width="50" height="50" viewBox="0 0 50 50" fill="#fff"><path d="M40 6l4 4-14 14-4-4z"/><path d="M24 22l6 6c-3 8-10 14-22 14 4-4 6-10 6-14 3-4 6-6 10-6z"/></svg></div>
    <h3>Data<br>Cleansing</h3>
    <p>Lorem Ipsum is simply dummy text of the printing and typesetting industry. Lorem Ipsum has been the</p>
  </div>

  <div class="btn btn-white" style="left:507px;top:533px;width:187px;height:40px">Learn More</div>
</section>

<h2 class="abs display section-title" style="left:150px;top:2182px">Contact Us</h2>
<div class="abs field" style="top:2282px">Name:</div>
<div class="abs field" style="top:2336px">Email Address:</div>
<div class="abs field" style="top:2390px">Phone No:</div>
<div class="abs field" style="top:2445px">Services Required
  <svg class="abs" style="left:432px;top:18px" width="8" height="5" viewBox="0 0 8 5"><path d="M0 0h8L4 5z" fill="var(--navy)"/></svg>
</div>
<div class="abs field" style="top:2498px;height:167px">Message:</div>
<div class="btn btn-navy" style="left:150px;top:2707px;width:167px;height:41px">Submit Now</div>
<div class="abs contact-photo" role="img" aria-label="Woman on a phone call taking notes at a desk"></div>

<footer class="abs footer">
  <div class="abs footer-brand">Kelvane Consulting</div>
  <p class="abs copyright">Copyright@2023-Kelvane-Privacy Policy</p>
  <nav class="abs footer-nav"><span>Home</span><span>About</span><span style="margin-left:12px">Services</span><span style="margin-left:8px">Contact</span></nav>
  <div class="abs social" style="left:772px" aria-label="Social link"></div>
  <div class="abs social" style="left:855px" aria-label="Social link"></div>
  <div class="abs social" style="left:937px" aria-label="Social link"></div>
  <div class="abs social" style="left:1019px" aria-label="Social link"></div>
</footer>

</body>
</html>
```